Business Card / Flyer Design Project

Prevent Accidents in your HomeSafety grab barsChild safety and child proofingEarthquake proofingOur company provide a service to help prevent home accidents of all types, from bathroom slip and fall accidents to baby proofing and earthquake safety. Maybe a 4x6 flyer type would be the best for handouts? Maybe a graphic of some kind? Company name, Dwelling Guard Crew. Contractors license # 731562

Contact Information for Business Card

Thad Friday818-419-4212

```html
<!DOCTYPE html>
<html lang="en">
<head>
<meta charset="utf-8">
<title>Dwelling Guard Crew – Flyer</title>
<link rel="stylesheet" href="https://fonts.googleapis.com/css2?family=Open+Sans:wght@400;600;700&display=swap">
<style>
  :root {
    --orange: #e8801f;
    --black: #111111;
    --white: #ffffff;
    --stage: #2a2a2a;
    --sage: #b9cf9a;
    --wood: #b9743a;
  }
  * { margin: 0; padding: 0; box-sizing: border-box; }
  html, body { width: 1200px; height: 960px; overflow: hidden; }
  body {
    background: var(--stage);
    font-family: "Open Sans", Arial, sans-serif;
    position: relative;
  }
  .card {
    position: absolute;
    left: 270px;
    width: 660px;
    height: 440px;
    overflow: hidden;
  }
  .card--front { top: 25px; }
  .card--back { top: 495px; }
  .card__art { position: absolute; inset: 0; }

  .brand {
    position: absolute;
    left: 0; right: 0;
    display: flex;
    align-items: center;
    justify-content: center;
    gap: 14px;
  }
  .brand__dot {
    border-radius: 50%;
    background: var(--orange);
    flex: none;
  }
  .brand__name {
    color: var(--orange);
    font-weight: 700;
    white-space: nowrap;
    line-height: 1.1;
  }
  .card--front .brand { top: 95px; }
  .card--front .brand__dot { width: 56px; height: 56px; }
  .card--front .brand__name { font-size: 38px; }

  .contact {
    position: absolute;
    left: 0; right: 0;
    top: 262px;
    text-align: center;
  }
  .contact__phone {
    color: var(--white);
    font-size: 34px;
    font-weight: 600;
    line-height: 1;
  }
  .contact__licence {
    color: var(--orange);
    font-size: 12px;
    font-weight: 600;
    margin-top: 4px;
  }
  .services {
    position: absolute;
    left: 0; right: 0;
    top: 335px;
    list-style: none;
    text-align: center;
    letter-spacing: 0.2em;
    font-size: 17px;
    font-weight: 600;
    line-height: 24px;
  }
  .services__item--accent { color: var(--orange); }
  .services__item--plain { color: var(--white); }

  .card--back .brand {
    top: 268px;
    flex-direction: column;
    gap: 12px;
  }
  .card--back .brand__dot { width: 64px; height: 64px; }
  .card--back .brand__name { font-size: 20px; }
</style>
</head>
<body>

<section class="card card--front">
  <svg class="card__art" viewBox="0 0 660 440" width="660" height="440">
    <rect width="660" height="440" fill="var(--white)"/>
    <path d="M0,120 Q330,330 660,130 L660,440 L0,440 Z" fill="var(--orange)"/>
    <path d="M0,165 Q330,345 660,165 L660,440 L0,440 Z" fill="var(--black)"/>
  </svg>

  <div class="brand">
    <span class="brand__dot"></span>
    <span class="brand__name">Dwelling Guard Crew</span>
  </div>

  <div class="contact">
    <p class="contact__phone">555-302-7186</p>
    <p class="contact__licence">LIC NO : 731562</p>
  </div>

  <ul class="services">
    <li class="services__item--accent">PREVENT ACCIDENTS IN YOUR HOME</li>
    <li class="services__item--plain">SAFETY GRAB BARS</li>
    <li class="services__item--accent">CHILD SAFETY AND CHILD PROOFING</li>
    <li class="services__item--plain">EARTHQUAKE PROOFING</li>
  </ul>
</section>

<section class="card card--back">
  <svg class="card__art" viewBox="0 0 660 440" width="660" height="440">
    <defs>
      <linearGradient id="bathPhoto" x1="0" y1="0" x2="0" y2="1">
        <stop offset="0" stop-color="#d5e4b8"/>
        <stop offset="1" stop-color="var(--sage)"/>
      </linearGradient>
      <linearGradient id="cabinetPhoto" x1="0" y1="0" x2="1" y2="1">
        <stop offset="0" stop-color="var(--wood)"/>
        <stop offset="1" stop-color="#4a2f1c"/>
      </linearGradient>
    </defs>
    <rect width="660" height="440" fill="var(--black)"/>
    <path d="M0,0 L273,0 Q328,170 178,440 L0,440 Z" fill="var(--orange)"/>
    <g role="img" aria-label="Photo of an older woman in a bathrobe holding a bathroom grab bar">
      <path d="M0,0 L265,0 Q320,170 170,440 L0,440 Z" fill="url(#bathPhoto)"/>
    </g>
    <path d="M660,0 L402,0 Q352,200 492,440 L660,440 Z" fill="var(--orange)"/>
    <g role="img" aria-label="Photo of a toddler reaching into an open kitchen cabinet">
      <path d="M660,0 L410,0 Q360,200 500,440 L660,440 Z" fill="url(#cabinetPhoto)"/>
    </g>
  </svg>

  <div class="brand">
    <span class="brand__dot"></span>
    <span class="brand__name">Dwelling Guard Crew</span>
  </div>
</section>

</body>
</html>
```